Hartwell Taproom Co Menu Design

I have an exisiting restaurant called Hartwell Taproom Co. We have an official logo and an existing menu. We need something more professional and vibrant. We are a great little brewpub and need our menu to reflect the same.
Updates

I have added our existing menu that has our logo on first page. Please use and insert menu items and pricing. Thank you for all your help! I really need a great look... also our web site is hartwelltaproomco.comĀ  that may help as well

I have been trying to uplaod pictures for the menu design today but for some reason I can not get them to upload on this site. Will keep trying and hope to have some posted soon.

I have submitted pictures to pixel harbor web administration and they will be posting to my project shortly.

All pictures have been posted for menu design. Thanks!

Industry/Entity Type

Restaurant

Requirements
Must have
• Great layout with pictures!!! Need it to be eye catching with current menu items and pricing. Needs to be a funtional format so I can easily changed to add or delete items as needed. I am looking for a one page menu that is 8 1/2 x 14 with front and back side print that will be placed in a clear menu cover.

```html
<!DOCTYPE html>
<html lang="en">
<head>
<meta charset="utf-8">
<title>Hartwell Taproom Co – Menu Page 4</title>
<link href="https://fonts.googleapis.com/css2?family=Arimo:wght@400;700&family=Cinzel:wght@400;700&display=swap" rel="stylesheet">
<style>
  :root {
    --bg: #ffffff;
    --brick: #8e1a1c;
    --brick-dark: #5a0c0e;
    --panel: #0b0b0b;
    --red: #d0222a;
    --gold: #f3a437;
    --white: #ffffff;
    --ink: #111111;
  }
  * { margin: 0; padding: 0; box-sizing: border-box; }
  html, body { width: 1200px; height: 1000px; overflow: hidden; background: var(--bg); }
  body { position: relative; font-family: "Arimo", Arial, sans-serif; }

  .menu-page { position: absolute; left: 329px; top: 43px; width: 533px; height: 862px; }
  .brick-wall {
    position: absolute; inset: 0;
    background: radial-gradient(ellipse at center, var(--brick) 30%, var(--brick-dark) 100%);
  }
  .menu-panel { position: absolute; left: 36px; top: 32px; width: 463px; height: 760px; background: var(--panel); }

  .brand-mark {
    position: absolute; left: 364px; top: 70px; width: 140px; height: 150px;
    display: flex; flex-direction: column; align-items: center; justify-content: center; gap: 8px;
  }
  .brand-dot { width: 56px; height: 56px; border-radius: 50%; background: var(--gold); }
  .brand-name {
    font-family: "Cinzel", serif; font-weight: 700; font-size: 15px; line-height: 18px;
    color: var(--gold); text-align: center;
  }

  .food-strip {
    position: absolute; left: 0; bottom: 0; width: 533px; height: 130px;
    background: linear-gradient(90deg, #8a3a1a 0%, #d9b15a 30%, #e6d3a8 45%, #5e8a3a 60%, #c4703e 75%, #b7c48a 100%);
  }

  .block { position: absolute; text-align: center; color: var(--white); font-size: 9.4px; line-height: 10.6px; }
  .col-left { left: 56px; width: 215px; }
  .col-right { left: 268px; width: 206px; }

  .page-title { position: absolute; left: 120px; width: 200px; top: 48px; text-align: center;
    font-family: "Cinzel", serif; font-weight: 700; font-size: 25px; letter-spacing: 2px; color: var(--white); }
  .section-title { font-family: "Cinzel", serif; font-size: 15.5px; line-height: 17px; letter-spacing: 1.2px; color: var(--red); }
  .section-kicker { font-weight: 700; font-size: 11px; color: var(--red); line-height: 12px; }
  .section-note { color: var(--red); font-size: 9.6px; line-height: 11px; }
  .item-name { font-weight: 700; font-size: 11px; line-height: 12.5px; color: var(--gold); }
  .item-desc { margin-top: 1px; }
  .item-price { font-weight: 700; font-size: 10px; margin-top: 5px; }

  .page-label { position: absolute; left: 0; width: 1140px; top: 922px; text-align: center;
    font-family: "Arimo", Arial, sans-serif; font-size: 36px; color: var(--ink); }
</style>
</head>
<body>
<main class="menu-page">
  <div class="brick-wall" role="img" aria-label="Red brick wall background"></div>
  <div class="menu-panel"></div>

  <div class="brand-mark">
    <span class="brand-dot"></span>
    <span class="brand-name">Hartwell Taproom Co</span>
  </div>

  <h1 class="page-title">MENU</h1>

  <section class="block col-left" style="top:84px">
    <p class="section-kicker">What The Tide Brought In</p>
    <p class="section-note">All seafood burgers are served with choice of sweet potato fries or side salad</p>
  </section>

  <article class="block col-left" style="top:122px">
    <p class="item-name">Salmon Bacon</p>
    <p class="item-desc">Wild Alaskan grilled salmon, apple wood smoked bacon, grilled onions, tomatoes, mixed greens and chipotle ranch dressing on Hawaiian bun</p>
    <p class="item-price">$11.95</p>
  </article>

  <article class="block col-left" style="top:192px">
    <p class="item-name">Lobster</p>
    <p class="item-desc">Succulent sweet grilled lobster is dressed with a Cajun slaw then topped with avocado and apple wood smoked bacon on a French brioche bun</p>
    <p class="item-price">$12.95</p>
  </article>

  <section class="block col-left" style="top:269px">
    <h2 class="section-title">SPECIALTY HOT SANDWICHES</h2>
    <p class="section-note" style="margin-top:9px">All our generous size grilled sandwiches come with choice of regular fries or side salad. Sub sweet potato fries for $1.00 extra only if not listed in order *Add avocado to any sandwich $0.95. Available bread choices are <i>Baguette</i>, <i>Sourdough</i> or <i>Bavarian Rye</i>. Split any plate $2.00 extra… comes with full sides on each plate.</p>
  </section>

  <article class="block col-left" style="top:410px">
    <p class="item-name">BBQ Pulled Pork</p>
    <p class="item-desc" style="margin-top:4px">Piled high on Hawaiian bun drizzled with BBQ sauce and topped with apple cider slaw and sweet potato fries</p>
    <p class="item-price">$9.95</p>
  </article>

  <article class="block col-left" style="top:473px">
    <p class="item-name">Pastrami And Swiss</p>
    <p class="item-desc">Deli style lean beef pastrami piled high with aged Swiss, sauerkraut and mustard on Bavarian rye bread</p>
    <p class="item-price">$9.95</p>
  </article>

  <article class="block col-left" style="top:532px">
    <p class="item-name">Chicken Caprese</p>
    <p class="item-desc">Our grilled mesquite chicken breast with tomato, basil pesto and provolone on a toasty baguette</p>
    <p class="item-price">$8.95</p>
  </article>

  <article class="block col-left" style="top:595px">
    <p class="item-name">Albacore Melt</p>
    <p class="item-desc">Made with celery, onion, dill and a “pinch” of cayenne for some kick. Served with lettuce, tomato and Swiss cheese on Bavarian rye bread</p>
    <p class="item-price">$8.95</p>
  </article>

  <article class="block col-left" style="top:669px">
    <p class="item-name">Beef Short Rib</p>
    <p class="item-desc">Slow roasted beef short rib dipped in veal au jus served on a French baguette with sweet potato fries</p>
    <p class="item-price" style="margin-top:7px">$11.95</p>
  </article>

  <section class="block col-right" style="top:195px">
    <h2 class="section-title">PERSONAL PIZZAS<br>(7 INCH)</h2>
    <p class="section-note" style="margin-top:3px">*7 inch pizza and side salad<br>combo for $8.25</p>
  </section>

  <article class="block col-right" style="top:252px">
    <p class="item-name">Portabella Roasted Red Pepper Pizza</p>
    <p class="item-desc">Basil pesto, mozzarella, red peppers, portabella mushroom, baby greens and parmesan cheese</p>
    <p class="item-price">$7.25</p>
  </article>

  <article class="block col-right" style="top:321px">
    <p class="item-name">Margarita Pizza</p>
    <p class="item-desc">Garlic infused olive oil, tomato sauce, mozzarella cheese, sliced tomatoes and pesto</p>
    <p class="item-price" style="margin-top:3px">$6.95</p>
  </article>

  <article class="block col-right" style="top:369px">
    <p class="item-name">BBQ Buffalo Chicken Pizza</p>
    <p class="item-desc">BBQ sauce, mozzarella, diced celery, red onions and grilled chicken breast marinated in buttery buffalo sauce drizzled with ranch dressing</p>
    <p class="item-price">$7.25</p>
  </article>

  <article class="block col-right" style="top:441px">
    <p class="item-name">Bleu Fire Chicken Pizza</p>
    <p class="item-desc">Fire glaze, mozzarella, bleu cheese, cheddar jack, portabella mushroom, mesquite chicken, scallions and cilantro</p>
    <p class="item-price">$7.25</p>
  </article>

  <section class="block col-right" style="top:509px">
    <h2 class="section-title">LUNCH SPECIALS</h2>
    <p class="section-title" style="font-size:13px;line-height:15px">MONDAY - FRIDAY</p>
    <p class="section-title" style="font-size:14px;line-height:16px">11:00AM - 3:00PM</p>
    <p class="section-note" style="margin-top:2px">(No Substitutions)</p>
  </section>

  <article class="block col-right" style="top:578px">
    <p class="item-name">Chicken Ceasar Salad</p>
    <p class="item-desc">(Lunch portion): Romaine lettuce and mesquite grilled chicken, focaccia croutons, parmesan cheese and Caesar dressing</p>
    <p class="item-price">$5.95</p>
  </article>

  <article class="block col-right" style="top:643px">
    <p class="item-name">Tinga De Pollo Quesadilla &amp; House Side Salad</p>
    <p class="item-desc">Grilled chicken is made in a cream sauce with caramelized onions, roasted peppers, smoked jalapeno, cilantro and Colby jack cheese on a flour tortilla and chipotle dipping sauce</p>
    <p class="item-price">$5.95</p>
  </article>

  <div class="food-strip" role="img" aria-label="Row of food photos: beers, chicken wings, pressed sandwich, mac and cheese, seared tuna, salad, pizza, chocolate dessert and Caesar salad"></div>
</main>

<p class="page-label">Page 4</p>
</body>
</html>
```